Business Card Design for new social media business

I am looking for a new professional business card design for an exciting new company which is based on providing members with experiences of others to benefit their choice of places to visit for restaurants, bars, clubs, national monument, tourist sights, hotels and so forth.
Updates

Please submit designs as I will choose to commit the funds depending on designs.

Target Market(s)

Business Managers as well as directors alongside owners

Industry/Entity Type

Business

Requirements
Must have
• Logo design and symbols
Nice to have
• Logo / Symbol on the back of the business card and possibly the logo as if embedded/embossed on the business card.

```html
<!DOCTYPE html>
<html lang="en">
<head>
<meta charset="utf-8">
<title>Wandrly Business Card</title>
<link rel="stylesheet" href="https://fonts.googleapis.com/css2?family=Montserrat:wght@600;700&family=Questrial&display=swap">
<style>
  :root {
    --backdrop: #1e2024;
    --card-white: #ffffff;
    --brand-blue: #2a67c4;
    --deep-blue: #1f55b0;
    --ink-blue: #2259b8;
    --charcoal: #3a3a3c;
    --text-dark: #333338;
    --text-grey: #5a5a5e;
    --rule-grey: #6b6b6e;
  }
  * { margin: 0; padding: 0; box-sizing: border-box; }
  html, body { width: 1200px; height: 675px; overflow: hidden; }
  body {
    background: var(--backdrop);
    font-family: "Questrial", "Century Gothic", sans-serif;
    position: relative;
  }
  .card {
    position: absolute;
    top: 184px;
    width: 540px;
    height: 308px;
    overflow: hidden;
    box-shadow: 0 12px 30px rgba(0,0,0,.45);
  }
  .card-front { left: 45px; background: var(--card-white); }
  .card-back {
    left: 615px;
    background: linear-gradient(135deg, var(--brand-blue), var(--deep-blue));
  }

  .wordmark {
    display: flex;
    align-items: center;
    gap: 10px;
    font-family: "Montserrat", sans-serif;
    font-weight: 700;
    letter-spacing: -0.5px;
    line-height: 1;
  }
  .wordmark-dot { border-radius: 50%; flex: none; }

  .front-mark {
    position: absolute;
    top: 34px;
    left: 0;
    right: 0;
    justify-content: center;
    font-size: 36px;
    color: var(--ink-blue);
  }
  .front-mark .wordmark-dot { width: 28px; height: 28px; background: var(--ink-blue); }

  .main-rule {
    position: absolute;
    top: 98px;
    left: 28px;
    right: 28px;
    height: 1px;
    background: var(--rule-grey);
  }

  .contact-list {
    position: absolute;
    top: 108px;
    right: 28px;
    list-style: none;
    text-align: right;
    font-size: 12.5px;
    line-height: 17px;
    color: var(--text-dark);
  }
  .contact-list li { display: flex; align-items: center; justify-content: flex-end; gap: 6px; }
  .contact-list svg { width: 10px; height: 10px; fill: var(--ink-blue); }

  .person {
    position: absolute;
    top: 150px;
    left: 28px;
  }
  .person-name {
    font-family: "Montserrat", sans-serif;
    font-weight: 700;
    font-size: 17px;
    color: var(--ink-blue);
  }
  .person-title { font-size: 14px; color: var(--text-dark); margin-top: 1px; }
  .person-rule { width: 200px; height: 1px; background: var(--rule-grey); margin: 9px 0 12px; }
  .address { font-size: 12.5px; line-height: 16px; color: var(--text-grey); font-style: normal; }

  .band-blue {
    position: absolute;
    left: 0; bottom: 0;
    width: 360px; height: 22px;
    background: var(--brand-blue);
  }
  .band-charcoal {
    position: absolute;
    right: 0; bottom: 0;
    width: 180px; height: 48px;
    background: var(--charcoal);
    display: flex;
    align-items: center;
    justify-content: center;
    color: #fff;
    font-family: "Montserrat", sans-serif;
    font-weight: 600;
    font-size: 12px;
  }

  .back-content {
    position: absolute;
    inset: 0;
    display: flex;
    flex-direction: column;
    align-items: center;
    justify-content: center;
    gap: 36px;
  }
  .back-mark { font-size: 46px; color: #fff; }
  .back-mark .wordmark-dot { width: 36px; height: 36px; background: #fff; }
  .back-url {
    color: #fff;
    font-family: "Montserrat", sans-serif;
    font-weight: 600;
    font-size: 12px;
  }
</style>
</head>
<body>
  <section class="card card-front">
    <div class="wordmark front-mark"><span class="wordmark-dot"></span>Wandrly</div>

    <div class="main-rule"></div>

    <ul class="contact-list">
      <li>555.201.4830
        <svg viewBox="0 0 10 10" aria-hidden="true"><path d="M1 3.5C1 2 2 1.5 5 1.5S9 2 9 3.5V4.5H7V3.5H3V4.5H1Z"/><rect x="1.5" y="5" width="7" height="4" rx="0.8"/></svg>
      </li>
      <li>555.348.7192
        <svg viewBox="0 0 10 10" aria-hidden="true"><rect x="3" y="0.5" width="4" height="9" rx="0.8"/></svg>
      </li>
      <li>marcus@wandrly.com
        <svg viewBox="0 0 10 10" aria-hidden="true"><path d="M0.5 2H9.5V8H0.5Z M0.5 2L5 5.5L9.5 2" stroke="#fff" stroke-width="0.6"/></svg>
      </li>
    </ul>

    <div class="person">
      <div class="person-name">Marcus Ellery</div>
      <div class="person-title">Principal</div>
      <div class="person-rule"></div>
      <address class="address">480 Harbor Lane<br>Riverton, IL 60000</address>
    </div>

    <div class="band-blue"></div>
    <div class="band-charcoal">www.wandrly.com</div>
  </section>

  <section class="card card-back">
    <div class="back-content">
      <div class="wordmark back-mark"><span class="wordmark-dot"></span>Wandrly</div>
      <div class="back-url">www.wandrly.com</div>
    </div>
  </section>
</body>
</html>
```